Startup company business card (Media & Advertising)

we need a business card design for a company that is a startup in the media and aggregation industry. Card needs to look funky and of a new breed/modern and upmarket.

Target Market(s)

advertisers/ brand agencies & media publishers

Industry/Entity Type

Advertising

Contact Information for Business Card

Please ensure the front face signifies our brand (plumvexo.com) and back has details for the contact. Standard contact such as phone , address, email , website etc.

Font styles to use
Other font styles liked:
• use styleguide and logo font and color

Colors

Designer to choose colors to be used in the design.

Requirements
Must have
• We are disrupting the media and agency industry so subtlety would be good to use imagery to signify this
Nice to have
• Please use logo colors for branding
Should not have
• be as creative and provide few options. Pick a brand color from logo and styleguide

```html
<!DOCTYPE html>
<html lang="en">
<head>
<meta charset="utf-8">
<title>plumvexo business card</title>
<link rel="stylesheet" href="https://fonts.googleapis.com/css2?family=Poppins:wght@400;500;600;700&display=swap">
<style>
  :root {
    --stage: #e9e9ec;
    --ink-dark: #23262b;
    --crowd-a: #3a3b3f;
    --crowd-b: #1c1d20;
    --paper-a: #ffffff;
    --paper-b: #d9d9dc;
    --red-light: #f0414a;
    --red-deep: #b81e3a;
    --white: #ffffff;
  }
  * { box-sizing: border-box; margin: 0; padding: 0; }
  html, body { width: 1200px; height: 800px; overflow: hidden; }
  body {
    background: var(--stage);
    font-family: "Poppins", sans-serif;
    display: flex;
    align-items: center;
    justify-content: center;
    gap: 40px;
  }
  .card {
    position: relative;
    width: 540px;
    height: 310px;
    border-radius: 22px;
    overflow: hidden;
  }

  /* Front face */
  .card-front .crowd-photo {
    position: absolute; inset: 0;
    background: radial-gradient(circle at 40% 40%, var(--crowd-a), var(--crowd-b));
  }
  .card-front .paper-reveal {
    position: absolute;
    left: 150px; top: 40px;
    width: 240px; height: 210px;
    border-radius: 46% 54% 50% 50% / 52% 46% 54% 48%;
    background: radial-gradient(circle at 50% 50%, var(--paper-a) 45%, var(--paper-b));
  }
  .brand {
    display: flex; align-items: center; gap: 10px;
    font-weight: 600;
  }
  .brand-dot { border-radius: 50%; background: var(--red-light); flex: none; }
  .card-front .brand {
    position: absolute; left: 0; right: 0; top: 138px;
    justify-content: center;
    font-size: 26px; color: var(--ink-dark);
  }
  .card-front .brand-dot { width: 24px; height: 24px; }

  /* Back face */
  .card-back .card-shapes { position: absolute; inset: 0; }
  .card-back .brand {
    position: absolute; left: 44px; top: 118px;
    font-size: 38px; color: var(--white);
  }
  .card-back .brand-dot { width: 38px; height: 38px; }
  .contact {
    position: absolute; right: 30px; top: 92px;
    color: var(--white);
    text-align: right;
  }
  .contact-name { font-size: 16px; font-weight: 700; letter-spacing: 0.5px; line-height: 1.1; }
  .contact-title { font-size: 9px; font-weight: 600; letter-spacing: 0.6px; margin-bottom: 8px; }
  .contact-line {
    display: flex; align-items: center; justify-content: flex-end; gap: 8px;
    font-size: 11px; line-height: 1.9;
  }
  .contact-line svg { width: 11px; height: 11px; flex: none; }
  .address {
    position: absolute; left: 44px; bottom: 24px;
    display: flex; align-items: flex-end; gap: 10px;
    color: var(--white); font-size: 12px; line-height: 1.6;
  }
  .address svg { width: 12px; height: 16px; margin-bottom: 4px; }
</style>
</head>
<body>

  <section class="card card-front">
    <div class="crowd-photo" role="img" aria-label="Photo of a large crowd of people in dark monochrome"></div>
    <div class="paper-reveal" role="img" aria-label="Torn paper opening revealing a white surface"></div>
    <div class="brand"><span class="brand-dot"></span><span>plumvexo</span></div>
  </section>

  <section class="card card-back">
    <svg class="card-shapes" viewBox="0 0 540 310" preserveAspectRatio="none" aria-hidden="true">
      <defs>
        <linearGradient id="red-fill" x1="0" y1="1" x2="1" y2="0">
          <stop offset="0" stop-color="var(--red-deep)"/>
          <stop offset="1" stop-color="var(--red-light)"/>
        </linearGradient>
      </defs>
      <rect width="540" height="310" fill="url(#red-fill)"/>
      <path d="M0,0 H318 C268,30 262,120 220,170 C180,215 90,218 0,212 Z" fill="#e03242" opacity="0.8" transform="translate(6,6)"/>
      <path d="M0,0 H318 C268,30 262,120 220,170 C180,215 90,218 0,212 Z" fill="var(--ink-dark)"/>
    </svg>

    <div class="brand"><span class="brand-dot"></span><span>plumvexo</span></div>

    <div class="contact">
      <p class="contact-name">DANA WHITLOW</p>
      <p class="contact-title">MANAGING DIRECTOR</p>
      <p class="contact-line">555-013-4820
        <svg viewBox="0 0 12 12"><path d="M2.5 1 L4.5 1 L5.3 3.5 L4 4.6 C4.7 6 6 7.3 7.4 8 L8.5 6.7 L11 7.5 L11 9.5 C11 10.3 10.3 11 9.5 11 C5 11 1 7 1 2.5 C1 1.7 1.7 1 2.5 1 Z" fill="var(--white)"/></svg>
      </p>
      <p class="contact-line">dana@plumvexo.com
        <svg viewBox="0 0 12 12"><rect x="1" y="2.5" width="10" height="7" rx="1" fill="var(--white)"/><path d="M1.5 3 L6 6.5 L10.5 3" stroke="var(--red-light)" stroke-width="1" fill="none"/></svg>
      </p>
      <p class="contact-line">www.plumvexo.com
        <svg viewBox="0 0 12 12"><circle cx="6" cy="6" r="5" fill="var(--white)"/><path d="M1 6 H11 M6 1 C3.5 3.5 3.5 8.5 6 11 M6 1 C8.5 3.5 8.5 8.5 6 11" stroke="var(--red-light)" stroke-width="0.8" fill="none"/></svg>
      </p>
    </div>

    <div class="address">
      <svg viewBox="0 0 12 16"><path d="M6 0 C2.7 0 0 2.6 0 5.9 C0 10 6 16 6 16 C6 16 12 10 12 5.9 C12 2.6 9.3 0 6 0 Z" fill="var(--white)"/><circle cx="6" cy="6" r="2.2" fill="var(--red-deep)"/></svg>
      <p>88 Larkspur Avenue NW<br>Suite 210, Fenwick Bay<br>MI 49000</p>
    </div>
  </section>

</body>
</html>
```